Visitenkarten-Design für Hausarztpraxis
Professionelle Arbeitsweise, kreative Ideen, flexible Kundenbetreuung Top in allen Punkten. Besser gehts nicht. Ich werde bald wieder auf die Designerin zurückkommen.
Zielgruppe
Hausarztpraxis mit Schwerpunkt Geriatrie
Zielgruppe: Patienten in einem eher ländlichen Stadtgebiet mit hoher Anzahl von Senioren
Aufgabenstellung
Idee: Kombination eines Gutscheines für eine Kaffespezialität auf der Rückseite und einer beschreibbaren Vorderseite als Bestellkärtchen mit Foto von zukünftigen "Praxisgängern" im Querschnitt. D.h. Zu sehen sein sollten 1 lustige Oma , 1 lustiger Opa (z.B. Pfeife rauchend), 1 Jugendlicher und diverse andere Erwachsene verschiedener Berufsgruppen. Beispielhaft siehe unter: Farbkobold: Online Terminvereinbarung-Die keine Wünsche offen lässt. Das Bild könnte auch "gezeichnet" sein. Ich würde aber ein treffendes Foto bevorzugen. Design: gut leserliche Schrift, keine verschlungene Schriftarten, wegen Lesbarkeit für Renterklientel.
Info auf der Vorderseite mit Foto: WARTEN? Nicht bei uns - Ihr persönlicher Wunschtermin:
Info auf der Rückseite (Gutschein): Gutschein für eine Kaffeespezialität (Kaffeesymbol)
farblich unterlegt, Farbe egal, passend abgestimmt zur Vorderseite
Zur Erklärung:
Die Form/ Grösse sollte die einer Visitenkarte möglichst nicht überschreiten. Gern auch eine grössere Visitenkartenform 10cm breit und 7,5 cm hoch. Das Format ist unserem Zeitdruck geschuldet. Es muss ein Werbemittel in 14 Tagen zur Praxiseröffnung zur Verfügung stehen, was sich schnell und kostengünstig produzieren und bei Bedarf ohne Probleme nachproduzieren lässt.
Sonderformate haben lange Auftragszeiten bei den auszuführenden Werbedruckfirmen.

```html
<!DOCTYPE html>
<html lang="de">
<head>
<meta charset="utf-8">
<title>Terminkarte und Kaffeegutschein</title>
<link rel="stylesheet" href="https://fonts.googleapis.com/css2?family=Share+Tech+Mono&display=swap">
<style>
  :root {
    --page: #ffffff;
    --ink: #1e1e1e;
    --panel-light: rgba(255, 255, 255, 0.72);
    --panel-solid: #ffffff;
    --panel-coffee: rgba(255, 255, 255, 0.5);
    --shadow: rgba(0, 0, 0, 0.45);
    --wait-top: #5d6c7e;
    --wait-mid: #8c98a6;
    --wait-floor: #dfe8ee;
    --bean-dark: #4a2412;
    --bean-mid: #8a4a26;
    --bean-light: #b56a3a;
  }
  * { box-sizing: border-box; margin: 0; padding: 0; }
  html, body {
    width: 849px;
    height: 1200px;
    overflow: hidden;
    background: var(--page);
  }
  body {
    position: relative;
    font-family: "Share Tech Mono", monospace;
    color: var(--ink);
  }
  .card {
    position: absolute;
    width: 687px;
    height: 444px;
    overflow: hidden;
    box-shadow: 3px 4px 5px var(--shadow);
  }
  .card--appointment { left: 73px; top: 60px; }
  .card--voucher { left: 72px; top: 641px; }

  .photo { position: absolute; inset: 0; }
  .photo--waiting-room {
    background: linear-gradient(180deg, var(--wait-top) 0%, var(--wait-mid) 45%, #b9c4cc 68%, var(--wait-floor) 78%, #eef3f6 100%);
  }
  .photo--coffee-beans {
    background: radial-gradient(circle at 30% 30%, var(--bean-light) 0%, transparent 45%),
                radial-gradient(circle at 75% 70%, var(--bean-light) 0%, transparent 40%),
                linear-gradient(135deg, var(--bean-mid) 0%, var(--bean-dark) 50%, var(--bean-mid) 100%);
  }

  .panel {
    position: absolute;
    text-align: center;
    font-variant: small-caps;
  }
  .panel--headline {
    left: 94px; top: 115px; width: 536px; height: 212px;
    background: var(--panel-light);
  }
  .panel--fields {
    left: 94px; top: 346px; width: 536px; height: 66px;
    background: var(--panel-solid);
    text-align: left;
  }
  .panel--voucher {
    left: 75px; top: 116px; width: 536px; height: 212px;
    background: var(--panel-coffee);
  }

  .headline {
    font-size: 36px;
    letter-spacing: 5px;
    line-height: 1;
    margin-top: 20px;
    font-weight: 400;
  }
  .subline {
    font-size: 30px;
    letter-spacing: 6px;
    line-height: 47px;
    margin-top: 8px;
  }
  .field {
    position: absolute;
    top: 16px;
    font-size: 31px;
    letter-spacing: 5px;
  }
  .field--date { left: 16px; }
  .field--time { left: 315px; }

  .voucher-title {
    font-size: 46px;
    letter-spacing: 6px;
    line-height: 1;
    margin-top: 37px;
    font-weight: 400;
  }
  .voucher-text {
    font-size: 29px;
    letter-spacing: 7px;
    line-height: 47px;
    margin-top: 8px;
  }
</style>
</head>
<body>
  <section class="card card--appointment">
    <div class="photo photo--waiting-room" role="img" aria-label="Foto: fünf Personen in Geschäftskleidung sitzen nebeneinander auf Stühlen im Wartebereich"></div>
    <div class="panel panel--headline">
      <h1 class="headline">WARTEN?</h1>
      <p class="subline">Nicht bei uns –<br>Ihr persönlicher<br>Wunschtermin</p>
    </div>
    <div class="panel panel--fields">
      <span class="field field--date">Wann</span>
      <span class="field field--time">Uhr</span>
    </div>
  </section>

  <section class="card card--voucher">
    <div class="photo photo--coffee-beans" role="img" aria-label="Foto: geröstete Kaffeebohnen, flächig"></div>
    <div class="panel panel--voucher">
      <h2 class="voucher-title">GUTSCHEIN</h2>
      <p class="voucher-text">über eine<br>Kaffespezialität</p>
    </div>
  </section>
</body>
</html>
```